Dr. Pelham Billboard Sign Design

Family Dental Practice looking for a billboard sign design. We have Attached a Image of Dr Pelham and Her horse she would like to incorporate. The size of the sign is 118" tall and 196" Wide. We hired a previous designer to work on this also but would like to see what other come up with before we decide on a final. Please use something similar for a animal shelter icon to go beside the Animal Shelter Discount statement. You can use the text from the postcard file attached. I know text adjustments will be needed, but more interested in a eye catching design. Themes: Fall/Winter/Mountains/Nature , colors: open but Dr P like purple. We are open to ideas and will answer any questions.
TEXT
Theme: Fall/Winter/Mountain
Image: Dr Pelham with Horse (Same from mailer design)
Text to Keep that needs to be bold and Priority
1. Dr. Rosalind Pelham Family Dentistry
417 Birch Lane Spruce Pine, NC 28704
828-555-3418 | RPelhamDDS@mailvexo.net
(FaceBook icon) RosalindPelhamDDS
2. ACCEPTING NEW PATIENTS
3. Affordable Dentistry for Your Whole Family
4. WE FILE YOUR INSURANCE CLAIMS
5. Discounts for Senior Citizens, Law Enforcement, First Responders, Military Personnel, State Employees and College Students
6. (Cool Animal Shelter Icon) WE OFFER A DISCOUNT TO PATIENTS WHO SUPPORT OUR LOCAL ANIMAL SHELTERS BY ADOPTING, DONATING OR VOLUNTEERING
7. Schedule Your Appointment TODAY!
Target Market(s)
Local Community to Bring in Patients to dental office
Industry/Entity Type
Dental
Look and feel

```html
<!DOCTYPE html>
<html lang="en">
<head>
<meta charset="utf-8">
<title>Dr. Pelham Family Dentistry Billboard</title>
<link href="https://fonts.googleapis.com/css2?family=Open+Sans:wght@400;600;700;800&display=swap" rel="stylesheet">
<style>
  :root {
    --page-bg: #e9e4dc;
    --night: #1f0a4a;
    --violet: #4a1590;
    --orchid: #8a2fc4;
    --band: #7c1790;
    --footer: #2a0c5e;
    --frame: #7d1a93;
    --yellow: #ffef00;
    --white: #ffffff;
    --ink: #2a0c5e;
    --photo-a: #8d8470;
    --photo-b: #5a4636;
  }
  * { margin: 0; padding: 0; box-sizing: border-box; }
  html, body { width: 853px; height: 1200px; overflow: hidden; background: var(--page-bg); }
  body { position: relative; font-family: "Open Sans", Arial, sans-serif; }

  .billboard-holder { position: absolute; left: 20px; top: 355px; width: 813px; height: 490px; box-shadow: 0 6px 18px rgba(0,0,0,.35); }
  .billboard {
    position: absolute; left: 0; top: 0; width: 913px; height: 550px;
    transform: scale(0.8905); transform-origin: 0 0; overflow: hidden;
    background: radial-gradient(ellipse at 70% 40%, var(--orchid) 0%, var(--violet) 45%, var(--night) 100%);
    white-space: nowrap;
  }
  .sky-dots { position: absolute; inset: 0; }

  .offer-band { position: absolute; left: 380px; top: 325px; width: 533px; height: 138px; background: var(--band); }
  .contact-band { position: absolute; left: 330px; top: 463px; width: 583px; height: 87px; background: var(--footer); }

  .portrait-frame { position: absolute; left: 0; top: 0; width: 440px; height: 550px; }

  .headline { position: absolute; right: 38px; top: 10px; text-align: right; color: var(--white); font-weight: 800; line-height: 1; text-shadow: 2px 2px 0 rgba(20,0,50,.45); }
  .headline .line-1 { font-size: 50px; letter-spacing: .5px; }
  .headline .line-2 { font-size: 38px; margin-top: 4px; }

  .practice-bar { position: absolute; left: 428px; top: 108px; width: 447px; height: 30px; background: var(--yellow); color: var(--ink); font-weight: 800; font-size: 17.5px; text-align: center; line-height: 30px; letter-spacing: 0; white-space: nowrap; overflow: hidden; }

  .service-list { position: absolute; right: 38px; top: 152px; list-style: none; text-align: right; color: var(--white); font-weight: 600; font-size: 19px; line-height: 22px; }
  .service-list li { position: relative; padding-right: 24px; margin-bottom: 8px; }
  .service-list li .tooth { position: absolute; right: 0; top: 4px; width: 10px; height: 12px; }

  .discount-note { position: absolute; right: 55px; top: 286px; text-align: right; color: var(--yellow); font-weight: 600; font-size: 13.4px; line-height: 18px; }

  .shelter-badge { position: absolute; left: 451px; top: 348px; width: 88px; height: 86px; background: #1c2f6e; border: 2px solid #b9c4e6; }

  .offer-copy { position: absolute; right: 38px; top: 340px; text-align: right; color: var(--white); }
  .offer-copy .offer-title { color: var(--yellow); font-weight: 800; font-size: 50px; line-height: 54px; }
  .offer-copy .offer-lead { font-size: 13.5px; font-weight: 400; line-height: 18px; }
  .offer-copy .offer-body { font-size: 13px; font-weight: 700; line-height: 18px; }

  .contact-item { position: absolute; display: flex; align-items: center; color: var(--yellow); font-weight: 700; font-size: 14.5px; }
  .contact-item svg { width: 22px; height: 22px; margin-right: 16px; flex: none; }
  .contact-email { left: 375px; top: 479px; font-size: 14px; }
  .contact-social { left: 375px; top: 512px; }
  .contact-address { left: 640px; top: 471px; font-size: 12.5px; line-height: 17px; align-items: flex-start; }
  .contact-address svg { margin-right: 10px; margin-top: 2px; }

  .phone-pill { position: absolute; left: 621px; top: 510px; width: 254px; height: 31px; background: var(--yellow); border-radius: 8px; display: flex; align-items: center; justify-content: center; color: var(--band); font-weight: 800; font-size: 26px; }
  .phone-pill svg { width: 20px; height: 20px; margin-right: 12px; }
</style>
</head>
<body>
<div class="billboard-holder">
  <div class="billboard">
    <svg class="sky-dots" viewBox="0 0 913 550" aria-hidden="true">
      <g fill="#ffffff" opacity=".7">
        <circle cx="452" cy="150" r="1.5"/><circle cx="520" cy="200" r="1"/><circle cx="610" cy="240" r="1.5"/>
        <circle cx="700" cy="180" r="1"/><circle cx="470" cy="260" r="1"/><circle cx="880" cy="300" r="1.5"/>
        <circle cx="430" cy="245" r="1"/><circle cx="560" cy="130" r="1"/>
      </g>
      <polygon points="490,158 495,172 510,172 498,181 502,195 490,186 478,195 482,181 470,172 485,172" fill="#c45bd8" opacity=".6"/>
    </svg>

    <div class="offer-band"></div>
    <div class="contact-band"></div>

    <svg class="portrait-frame" viewBox="0 0 440 550">
      <defs>
        <linearGradient id="photoTone" x1="0" y1="0" x2="1" y2="1">
          <stop offset="0" stop-color="var(--photo-a)"/>
          <stop offset="1" stop-color="var(--photo-b)"/>
        </linearGradient>
      </defs>
      <path d="M0,0 L0,550 L300,550 C360,450 415,330 410,215 C405,90 330,0 240,0 Z" fill="var(--frame)"/>
      <path d="M0,10 C40,20 95,45 120,70 C150,25 200,0 245,2 C345,8 400,100 398,215 C396,330 340,450 280,550 L262,550 C320,450 372,330 372,220 C372,110 320,40 250,38 C200,37 160,60 128,95 C100,70 50,50 0,44 Z" fill="var(--white)"/>
      <path d="M0,44 C50,50 100,70 128,95 C160,60 200,37 250,38 C320,40 372,110 372,220 C372,330 320,450 262,550 L0,550 Z" fill="url(#photoTone)" role="img" aria-label="Photo of Dr. Pelham standing beside her brown horse with a white blaze"/>
      <path d="M0,550 L0,505 C50,470 140,465 215,500 C235,512 250,530 262,550 Z" fill="var(--night)"/>
      <path d="M0,505 C50,470 140,465 215,500 C235,512 250,530 262,550 L250,550 C235,525 210,508 190,500 C130,478 50,485 0,515 Z" fill="var(--frame)"/>
    </svg>

    <h1 class="headline">
      <div class="line-1">SCHEDULE YOUR</div>
      <div class="line-2">APPOINTMENT TODAY!</div>
    </h1>

    <div class="practice-bar">DR. ROSALIND PELHAM FAMILY DENTISTRY</div>

    <ul class="service-list">
      <li>ACCEPTING NEW PATIENTS<svg class="tooth" viewBox="0 0 10 12"><path d="M0,2 C0,-1 4,0 5,1 C6,0 10,-1 10,2 C10,6 8,7 8,12 L6,12 L5,8 L4,12 L2,12 C2,7 0,6 0,2 Z" fill="var(--yellow)"/></svg></li>
      <li>WE FILE YOUR<br>INSURANCE CLAIMS<svg class="tooth" viewBox="0 0 10 12"><path d="M0,2 C0,-1 4,0 5,1 C6,0 10,-1 10,2 C10,6 8,7 8,12 L6,12 L5,8 L4,12 L2,12 C2,7 0,6 0,2 Z" fill="var(--yellow)"/></svg></li>
      <li>AFFORDABLE DENTISTRY<br>FOR YOUR WHOLE FAMILY<svg class="tooth" viewBox="0 0 10 12"><path d="M0,2 C0,-1 4,0 5,1 C6,0 10,-1 10,2 C10,6 8,7 8,12 L6,12 L5,8 L4,12 L2,12 C2,7 0,6 0,2 Z" fill="var(--yellow)"/></svg></li>
    </ul>

    <p class="discount-note">Discounts For Senior Citizens, Law Enforcement, First Responders,<br>Military Personnel, State Employees And College Students</p>

    <div class="shelter-badge" role="img" aria-label="Animal shelter badge"></div>

    <div class="offer-copy">
      <div class="offer-title">WE OFFER</div>
      <div class="offer-lead">A DISCOUNT TO PATIENTS</div>
      <div class="offer-body">WHO SUPPORT OUR LOCAL ANIMAL SHELTERS BY<br>ADOPTING, DONATING OR VOLUNTEERING</div>
    </div>

    <div class="contact-item contact-email">
      <svg viewBox="0 0 22 22"><circle cx="11" cy="11" r="10" fill="none" stroke="var(--yellow)" stroke-width="1.5"/><rect x="5.5" y="7" width="11" height="8" fill="none" stroke="var(--yellow)" stroke-width="1.4"/><path d="M5.5,7 L11,12 L16.5,7" fill="none" stroke="var(--yellow)" stroke-width="1.4"/></svg>
      RPelhamDDS@mailvexo.net
    </div>
    <div class="contact-item contact-social">
      <svg viewBox="0 0 22 22"><circle cx="11" cy="11" r="10" fill="none" stroke="var(--yellow)" stroke-width="1.5"/></svg>
      RosalindPelhamDDS
    </div>
    <div class="contact-item contact-address">
      <svg viewBox="0 0 22 22"><circle cx="11" cy="11" r="10" fill="none" stroke="var(--yellow)" stroke-width="1.5"/><path d="M11,17 C8,13 7,11 7,9.5 A4,4 0 0 1 15,9.5 C15,11 14,13 11,17 Z" fill="none" stroke="var(--yellow)" stroke-width="1.4"/><circle cx="11" cy="9.5" r="1.4" fill="var(--yellow)"/></svg>
      <span>417 Birch Lane Spruce Pine,<br>NC 28704</span>
    </div>

    <div class="phone-pill">
      <svg viewBox="0 0 22 22"><circle cx="11" cy="11" r="10" fill="none" stroke="var(--band)" stroke-width="1.6"/><path d="M7,6 L9,6 L10,9 L8.7,10 C9.5,11.8 10.5,12.8 12,13.3 L13,12 L16,13 L16,15 C16,15.6 15.5,16 15,16 C10.5,15.7 6.3,11.5 6,7 C6,6.5 6.4,6 7,6 Z" fill="var(--band)"/></svg>
      828-555-3418
    </div>
  </div>
</div>
</body>
</html>
```